Western Canadian Survey Company needs Business Card and Letter Head Design

Hello,

We're looking to have our business cards redesigned along with our letterhead.

We've recently changed out logo and would like to use this. Please use some creativity and propose different options (Traditional and modern).

We will provide as much feedback as possible.

Business card should be double sided with our logo. We would also like room for cell phone number, email address and position. Back of the card can just be our logo or potentially a list of our services we provide.

Industry/Entity Type

Business

Contact Information for Business Card

```html
<!DOCTYPE html>
<html lang="en">
<head>
<meta charset="utf-8">
<title>Ridgeline Survey Works — Stationery</title>
<link href="https://fonts.googleapis.com/css2?family=Montserrat:wght@400;500;700&display=swap" rel="stylesheet">
<style>
  :root {
    --ink: #0e0e0f;
    --slate: #56626f;
    --paper: #f4f4f5;
    --stage: #e6e7e9;
    --muted: #6d7278;
    --light-text: #e9ecef;
  }
  * { box-sizing: border-box; margin: 0; padding: 0; }
  html, body { width: 1200px; height: 874px; overflow: hidden; }
  body {
    background: var(--stage);
    font-family: "Montserrat", Arial, sans-serif;
    color: var(--ink);
    position: relative;
  }

  /* Brand lockup */
  .brand { display: flex; align-items: center; gap: 8px; font-weight: 700; letter-spacing: 0.08em; text-transform: uppercase; }
  .brand-mark { width: 14px; height: 14px; background: currentColor; flex: none; }
  .brand--dark { color: var(--ink); }
  .brand--light { color: #ffffff; }

  /* Letterhead */
  .letterhead {
    position: absolute; left: 70px; top: 90px;
    width: 480px; height: 680px;
    background: var(--paper);
    box-shadow: 0 10px 28px rgba(0,0,0,0.16);
    display: flex; flex-direction: column;
  }
  .letterhead-header { padding: 46px 48px 0; display: flex; justify-content: center; }
  .letterhead-header .brand { font-size: 17px; }
  .letterhead-rule { height: 2px; background: var(--slate); margin: 10px 140px 0; }
  .letter-body { padding: 48px 48px 0; font-size: 9.5px; line-height: 1.65; color: #3a3d41; flex: 1; }
  .letter-body p { margin-bottom: 11px; }
  .letter-sign { margin-top: 22px; }
  .letter-sign .signer { font-weight: 700; color: var(--ink); margin-top: 26px; }
  .letterhead-footer { background: var(--ink); color: var(--light-text); font-size: 8px; letter-spacing: 0.04em; padding: 11px 28px; display: flex; justify-content: space-between; }
  .letterhead-stripe { height: 8px; background: var(--slate); }

  /* Business cards */
  .card {
    position: absolute; left: 650px;
    width: 440px; height: 252px;
    box-shadow: 0 10px 24px rgba(0,0,0,0.16);
    overflow: hidden;
  }
  .card--front { top: 120px; background: var(--paper); display: flex; }
  .card--back { top: 450px; background: var(--ink); display: flex; flex-direction: column; }

  .card-strip { width: 46px; background: var(--ink); display: flex; flex-direction: column; justify-content: center; align-items: center; gap: 14px; border-right: 6px solid var(--slate); }
  .card-strip svg { width: 14px; height: 14px; fill: none; stroke: #fff; stroke-width: 1.6; }
  .card-content { flex: 1; padding: 26px 26px 22px; display: flex; flex-direction: column; }
  .card-content .brand { font-size: 13px; align-self: flex-end; }
  .card-content .brand-rule { height: 2px; background: var(--slate); width: 150px; align-self: flex-end; margin-top: 7px; }
  .card-details { margin-top: auto; display: flex; justify-content: space-between; align-items: flex-end; }
  .person-name { font-size: 15px; font-weight: 700; letter-spacing: 0.06em; text-transform: uppercase; }
  .person-role { font-size: 9px; color: var(--muted); margin-top: 3px; letter-spacing: 0.05em; }
  .contact-list { list-style: none; font-size: 8.5px; line-height: 1.9; color: #33363a; margin-top: 12px; }
  .card-address { font-size: 8.5px; line-height: 1.7; color: #33363a; text-align: right; }

  .card-back-main { flex: 1; display: flex; flex-direction: column; align-items: center; justify-content: center; gap: 10px; }
  .card-back-main .brand { font-size: 17px; }
  .card-back-main .brand-rule { height: 2px; width: 200px; background: var(--slate); }
  .card-web { font-size: 8.5px; color: #b9bfc6; letter-spacing: 0.08em; }
  .card-back-stripe { height: 26px; background: var(--slate); }
</style>
</head>
<body>

<section class="letterhead" aria-label="Letterhead">
  <header class="letterhead-header">
    <div class="brand brand--dark"><span class="brand-mark"></span>Ridgeline Survey Works Ltd</div>
  </header>
  <div class="letterhead-rule"></div>
  <div class="letter-body">
    <p>Dear Sir,</p>
    <p>Thank you for considering our team for your upcoming site work. We provide accurate layout, topographic and legal surveys for builders across the region.</p>
    <p>Our crews use modern equipment and careful field checks so every stake, line and elevation is right the first time.</p>
    <p>Please contact our office with any questions. We look forward to working with you.</p>
    <div class="letter-sign">
      <p>Yours Sincerely,</p>
      <p class="signer">Mara Ellison</p>
    </div>
  </div>
  <footer class="letterhead-footer">
    <span>118 Cedar Bench Road, Kamloops, BC V2C 4L7</span>
    <span>+1 250 555 0148</span>
    <span>www.ridgelinesurveyworks.ca</span>
  </footer>
  <div class="letterhead-stripe"></div>
</section>

<section class="card card--front" aria-label="Business card front">
  <div class="card-strip">
    <svg viewBox="0 0 16 16" aria-label="Phone"><path d="M4 2h3l1 3-2 1a8 8 0 0 0 4 4l1-2 3 1v3a1 1 0 0 1-1 1A12 12 0 0 1 3 3a1 1 0 0 1 1-1z"/></svg>
    <svg viewBox="0 0 16 16" aria-label="Email"><rect x="2" y="4" width="12" height="9"/><path d="M2 4l6 5 6-5"/></svg>
    <svg viewBox="0 0 16 16" aria-label="Address"><path d="M8 15s5-5 5-9A5 5 0 0 0 3 6c0 4 5 9 5 9z"/><circle cx="8" cy="6" r="1.8"/></svg>
  </div>
  <div class="card-content">
    <div class="brand brand--dark"><span class="brand-mark"></span>Ridgeline Survey Works</div>
    <div class="brand-rule"></div>
    <div class="card-details">
      <div>
        <p class="person-name">Jordan Hale</p>
        <p class="person-role">General Manager</p>
        <ul class="contact-list">
          <li>Cell: +1 250 555 0173</li>
          <li>Office: +1 250 555 0148</li>
          <li>office@ridgelinesurveyworks.ca</li>
        </ul>
      </div>
      <p class="card-address">118 Cedar Bench Road<br>Kamloops, BC V2C 4L7</p>
    </div>
  </div>
</section>

<section class="card card--back" aria-label="Business card back">
  <div class="card-back-main">
    <div class="brand brand--light"><span class="brand-mark"></span>Ridgeline Survey Works</div>
    <div class="brand-rule"></div>
    <p class="card-web">www.ridgelinesurveyworks.ca</p>
  </div>
  <div class="card-back-stripe"></div>
</section>

</body>
</html>
```